BrambleWorks business card

Looking for business card design that supports our company/software values. We have 2 logo designs at the moment but open to change if you think you can enhance the brand. Check out website www.brambleworks.com.au.

Target Market(s)

Education

Contact Information for Business Card

Name, title, mobile, email and website

Font styles to use
Sans Serif

Colors

Designer to choose colors to be used in the design.

Requirements
Must have
• BrambleWorks logo with tree and tagline on rear side with dark grey background colour

```html
<!DOCTYPE html>
<html lang="en">
<head>
<meta charset="utf-8">
<title>BrambleWorks business card</title>
<link rel="stylesheet" href="https://fonts.googleapis.com/css2?family=Raleway:wght@300;400&family=Ubuntu:wght@400&display=swap">
<style>
  :root {
    --backdrop: #222628;
    --card-light: #ffffff;
    --card-dark: #444444;
    --brand-green: #3daf48;
    --ink-dark: #1f1f1f;
    --ink-mid: #5b5b5b;
    --ink-soft: #555555;
    --ink-light: #dedede;
  }
  * { margin: 0; padding: 0; box-sizing: border-box; }
  html, body {
    width: 1200px;
    height: 1176px;
    overflow: hidden;
    background: var(--backdrop);
  }
  .canvas {
    position: relative;
    width: 1200px;
    height: 1176px;
  }
  .card {
    position: absolute;
    left: 280px;
    width: 617px;
    height: 352px;
    border-radius: 18px;
    overflow: hidden;
  }
  .card--front { top: 190px; background: var(--card-light); }
  .card--back { top: 590px; background: var(--card-dark); }

  /* Front */
  .front-brand {
    position: absolute;
    top: 40px;
    left: 0;
    width: 100%;
    display: flex;
    flex-direction: column;
    align-items: center;
  }
  .brand-dot {
    width: 76px;
    height: 76px;
    border-radius: 50%;
    background: var(--brand-green);
  }
  .front-brand .brand-name {
    margin-top: 18px;
    font-family: "Ubuntu", sans-serif;
    font-size: 28px;
    color: var(--ink-dark);
    line-height: 1;
  }
  .holder {
    position: absolute;
    top: 222px;
    right: 345px;
    text-align: right;
  }
  .holder-name {
    font-family: "Raleway", sans-serif;
    font-weight: 400;
    font-size: 31px;
    color: var(--ink-mid);
    line-height: 1;
  }
  .holder-title {
    margin-top: 5px;
    font-family: "Raleway", sans-serif;
    font-size: 14px;
    color: var(--brand-green);
    letter-spacing: 0.3px;
  }
  .divider {
    position: absolute;
    left: 308px;
    top: 211px;
    width: 2px;
    height: 96px;
    background: var(--brand-green);
  }
  .contacts {
    position: absolute;
    left: 339px;
    top: 222px;
    list-style: none;
  }
  .contacts li {
    display: flex;
    align-items: center;
    height: 26px;
    font-family: "Ubuntu", sans-serif;
    font-size: 15px;
    color: var(--ink-soft);
  }
  .contacts svg {
    width: 13px;
    height: 13px;
    margin-right: 10px;
    flex: none;
  }
  .accent-band {
    position: absolute;
    left: 0;
    bottom: 0;
    width: 100%;
    height: 20px;
    background: var(--brand-green);
  }

  /* Back */
  .back-lockup {
    position: absolute;
    top: 124px;
    left: 100px;
    display: flex;
    align-items: center;
  }
  .back-lockup .brand-dot {
    width: 92px;
    height: 92px;
    margin-right: 70px;
  }
  .back-text .brand-name {
    font-family: "Ubuntu", sans-serif;
    font-size: 46px;
    color: var(--ink-light);
    line-height: 1;
    padding-bottom: 10px;
    border-bottom: 2px solid var(--ink-light);
  }
  .tagline {
    margin-top: 6px;
    font-family: "Ubuntu", sans-serif;
    font-size: 19px;
    color: var(--ink-light);
    text-align: center;
  }
</style>
</head>
<body>
<main class="canvas">
  <section class="card card--front">
    <div class="front-brand">
      <span class="brand-dot"></span>
      <span class="brand-name">BrambleWorks</span>
    </div>
    <div class="holder">
      <p class="holder-name">Daniel Marlowe</p>
      <p class="holder-title">JOB TITLE</p>
    </div>
    <span class="divider"></span>
    <ul class="contacts">
      <li>
        <svg viewBox="0 0 16 16" aria-hidden="true"><path fill="var(--brand-green)" d="M4 1l3 3-1.6 2a9 9 0 0 0 4.6 4.6L12 9l3 3-2 3C7 15 1 9 1 3z"/></svg>
        000 000 0000
      </li>
      <li>
        <svg viewBox="0 0 16 16" aria-hidden="true"><rect x="1" y="3" width="14" height="10" fill="var(--brand-green)"/><path d="M1.5 3.5L8 9l6.5-5.5" fill="none" stroke="#fff" stroke-width="1.3"/></svg>
        youremail@abc.com
      </li>
      <li>
        <svg viewBox="0 0 16 16" aria-hidden="true"><g fill="none" stroke="var(--brand-green)" stroke-width="1.2"><circle cx="8" cy="8" r="6.5"/><ellipse cx="8" cy="8" rx="3" ry="6.5"/><path d="M1.5 8h13M2.5 4.8h11M2.5 11.2h11"/></g></svg>
        www.brambleworks.com.au
      </li>
    </ul>
    <span class="accent-band"></span>
  </section>

  <section class="card card--back">
    <div class="back-lockup">
      <span class="brand-dot"></span>
      <div class="back-text">
        <p class="brand-name">BrambleWorks</p>
        <p class="tagline">Student Success Platform</p>
      </div>
    </div>
  </section>
</main>
</body>
</html>
```